TV - business card

Tidewell Vantage is an insurance brokerage firm, inovative, proactive, vigorous, which aims to become the leader of the insurance brokers in Anfrica. We should like to get some designs which should be avoided also in Gray / Metallic for the Administration and Orange / Blue for the Managers (ike in the picture sent). The Blue / Green logo is not the correct one, but the source of the file. Please adjust the color accordingly for the business cards. 1 / Orange / Blue 2 / Gray / Metallic We want something classic but which is transmitted strenght, inovation, modernity and most of all, rapidity. We want something start-up like, very punchy and catching eye remaining profesional at the same time. Name: Delton Ashgrove Function: Managing Director Address: N ° 73/74 Cmt. Bolembe - R / C 2B Esquerda - Bairro Quimbuta - Luanda Tel: (+244) 947 385 619 Email: delton.ashgrove@tidewell-v.com Website: www.tidewell-v. com We want classic in the front and creative, colorfull at the back. The cards will be printed in relief, with very high quality of paper.
Industry/Entity Type
Insurance Broker
Colors
Designer to choose colors to be used in the design.
Look and feel

```html
<!DOCTYPE html>
<html lang="en">
<head>
<meta charset="utf-8">
<title>Tidewell Vantage – Business Card</title>
<link href="https://fonts.googleapis.com/css2?family=Lato:wght@300;400;700&display=swap" rel="stylesheet">
<style>
  :root {
    --backdrop: #141414;
    --card: #202020;
    --card-edge: #2a2a2a;
    --silver: #b9b9b9;
    --silver-soft: #8e8e8e;
    --divider: #3a3a3a;
  }
  html, body {
    margin: 0;
    padding: 0;
    width: 1200px;
    height: 900px;
    overflow: hidden;
    background: var(--backdrop);
  }
  .canvas {
    position: relative;
    width: 1200px;
    height: 900px;
    font-family: "Lato", sans-serif;
  }
  .card {
    position: absolute;
    width: 560px;
    height: 330px;
    border-radius: 26px;
    background: var(--card);
    border: 1px solid var(--card-edge);
    box-sizing: border-box;
  }
  .card-front { left: 120px; top: 80px; }
  .card-back  { left: 520px; top: 490px; }

  .brand {
    position: absolute;
    left: 0; right: 0; top: 0; bottom: 0;
    display: flex;
    align-items: center;
    justify-content: center;
    gap: 16px;
  }
  .brand-dot {
    width: 40px;
    height: 40px;
    border-radius: 50%;
    background: var(--silver);
  }
  .brand-name {
    color: var(--silver);
    font-weight: 700;
    font-size: 30px;
    letter-spacing: 1px;
    text-transform: uppercase;
  }

  .back-mark {
    position: absolute;
    left: 50px;
    top: 85px;
    width: 160px;
    height: 160px;
  }
  .back-divider {
    position: absolute;
    left: 255px;
    top: 60px;
    width: 1px;
    height: 210px;
    background: var(--divider);
  }
  .contact {
    position: absolute;
    left: 280px;
    top: 62px;
    color: var(--silver-soft);
    font-size: 14px;
    line-height: 1.35;
  }
  .contact-name {
    color: var(--silver);
    font-weight: 400;
    font-size: 19px;
    letter-spacing: 0.5px;
    text-transform: uppercase;
    margin: 0;
  }
  .contact-role { margin: 0 0 10px; font-size: 14px; }
  .contact-line { display: flex; align-items: center; gap: 7px; margin: 0; }
  .contact-line svg { width: 13px; height: 13px; fill: var(--silver-soft); flex: none; }
  .contact-address { margin: 12px 0 0; font-size: 15px; }
</style>
</head>
<body>
<main class="canvas">
  <section class="card card-front" aria-label="Card front">
    <div class="brand">
      <span class="brand-dot"></span>
      <span class="brand-name">Tidewell Vantage</span>
    </div>
  </section>

  <section class="card card-back" aria-label="Card back">
    <svg class="back-mark" viewBox="0 0 160 160" aria-hidden="true">
      <circle cx="80" cy="80" r="74" fill="none" stroke="#8a8a8a" stroke-width="8"/>
    </svg>
    <div class="back-divider"></div>
    <div class="contact">
      <p class="contact-name">Delton Ashgrove</p>
      <p class="contact-role">Managing Director</p>
      <p class="contact-line">
        <svg viewBox="0 0 24 24"><path d="M6.6 10.8a15 15 0 0 0 6.6 6.6l2.2-2.2a1 1 0 0 1 1-.25 11.4 11.4 0 0 0 3.6.57 1 1 0 0 1 1 1V20a1 1 0 0 1-1 1A17 17 0 0 1 3 4a1 1 0 0 1 1-1h3.5a1 1 0 0 1 1 1c0 1.25.2 2.45.57 3.57a1 1 0 0 1-.25 1z"/></svg>
        (+244) 947 385 619
      </p>
      <p class="contact-line">
        <svg viewBox="0 0 24 24"><path d="M2 5h20v14H2zM3.5 6.5 12 13l8.5-6.5z"/></svg>
        delton.ashgrove@tidewell-v.com
      </p>
      <p class="contact-address">
        N° 73/74 Cmt. Bolembe - R / C<br>
        2B Esquerda<br>
        Bairro Quimbuta - Luanda
      </p>
    </div>
  </section>
</main>
</body>
</html>
```